Refresh American History Book Cover

We would like a new book cover based on the attached old book cover. Please maintain a very strong resemblance to the cover, but we would be open to a bit of a freshening up of the design. We would like to use the same illustrations since they match the illustrations inside. Please fix the whale! It's head should not be cut off!

We are using this for Vextora Quillmark Self Printing in a 6" x 9" format.

```html
<!DOCTYPE html>
<html lang="en">
<head>
<meta charset="UTF-8">
<title>Wizards, Waves, Crinolines, &amp; Masts — Book Cover</title>
<link rel="stylesheet" href="https://fonts.googleapis.com/css2?family=Playfair+Display:ital,wght@1,700;1,900&family=Jost:wght@600&display=swap">
<style>
  :root {
    --stage: #f4f4f2;
    --paper: #ffffff;
    --title-blue: #1a6cf0;
    --accent-red: #e0301e;
    --art-red-soft: #fbe3df;
    --art-red-mid: #f6c4bb;
    --ink: #111111;
  }
  html, body {
    margin: 0;
    width: 1200px;
    height: 1200px;
    overflow: hidden;
    background: var(--stage);
  }
  .cover {
    position: absolute;
    left: 240px;
    top: 60px;
    width: 720px;
    height: 1080px;
    background: var(--paper);
    box-shadow: 0 6px 30px rgba(0,0,0,0.08);
    overflow: hidden;
  }
  .illustration {
    position: absolute;
    z-index: 0;
  }
  .illustration--whale {
    left: 0;
    top: 217px;
    width: 245px;
    height: 175px;
    border-radius: 40% 50% 45% 40%;
    background: radial-gradient(ellipse at 55% 45%, var(--art-red-mid), var(--art-red-soft) 70%, rgba(251,227,223,0) 100%);
  }
  .illustration--ship {
    left: 361px;
    top: 502px;
    width: 345px;
    height: 270px;
    border-radius: 30% 30% 12% 12%;
    background: radial-gradient(ellipse at 55% 55%, var(--art-red-mid), var(--art-red-soft) 70%, rgba(251,227,223,0) 100%);
  }
  .title {
    margin: 0;
    position: absolute;
    inset: 0;
    z-index: 1;
    font-family: "Playfair Display", Georgia, serif;
    font-style: italic;
    font-weight: 900;
    color: var(--title-blue);
    font-size: 118px;
    line-height: 1;
    letter-spacing: -1px;
  }
  .title__line {
    position: absolute;
    white-space: nowrap;
  }
  .title__line--first { left: 142px; top: 108px; }
  .title__line--second { left: 240px; top: 246px; }
  .title__line--third { left: 78px; top: 382px; }
  .title__line--fourth { left: 78px; top: 532px; }
  .subtitle {
    position: absolute;
    left: 0;
    right: 0;
    top: 820px;
    margin: 0;
    text-align: center;
    font-family: "Jost", "Futura", sans-serif;
    font-weight: 600;
    font-size: 24px;
    line-height: 33px;
    letter-spacing: 0.8px;
    color: var(--ink);
    text-transform: uppercase;
  }
  .author {
    position: absolute;
    left: 0;
    right: 0;
    top: 966px;
    margin: 0;
    text-align: center;
    font-family: "Playfair Display", Georgia, serif;
    font-style: italic;
    font-weight: 700;
    font-size: 46px;
    color: var(--accent-red);
  }
</style>
</head>
<body>
  <main class="cover">
    <div class="illustration illustration--whale" role="img" aria-label="Red line drawing of a whale arching out of the waves and spouting, shown in full with its head intact"></div>
    <div class="illustration illustration--ship" role="img" aria-label="Red line drawing of a three-masted sailing ship with full sails and pennants on the sea"></div>

    <h1 class="title">
      <span class="title__line title__line--first">Wizards,</span>
      <span class="title__line title__line--second">Waves,</span>
      <span class="title__line title__line--third">Crinolines,</span>
      <span class="title__line title__line--fourth">&amp; Masts</span>
    </h1>

    <p class="subtitle">Adventures and Misadventures from<br>Three Centuries of North Shore History</p>

    <p class="author">Dorothea Wakefield</p>
  </main>
</body>
</html>
```